Food company business card needs a freshen up

A little bit about our business. Wholesale Food Company (Vela Nu PNG Ltd) with a number of retail businesses including a Deli Butchery/Bakery (named The Bova Grill Yard) and Fast-Food Restaurants (Condor Wraps, Tam Lok Ret, Reefies) and a catering company called Bova Lulu Catering. At our head office (Vela Nu) we also have 2 manufacturing factories - Bakery (Bova Oven Loft products) and Butchery (Bova Fine products). We are proudly 100% PNG owned - this could be good to include somewhere on the business card.
Our current website is:
www.vnq-sample.com.pg
Please visit our website for further design aesthetics that we would like to tie into our business cards and information can be found on our website. Colour schemes are red, black and white.
We have a previous draft business card (attached) that we want to be improved to match our new website aesthetics.
We would like to make the business cards portrait and individualised for each of our staff members that require them and would like these to be editable to change the details when needed. We want these to be modern, professional and visually engaging with the use of photos (stock images used in our draft). If we can get photos of meat/sausages, fresh uncooked chicken, fresh fish, potato fries, cheese burger, bread roll/pies, and vegetables (make it look green and fresh) – these should be generic photos and product focused.
Constant information we want to see on the business cards.
1. Vela Nu PNG LTD
- Wholesale Food Sales & Delivery
- Butchery Manufacturing
- Bakery Manufacturing
- Quality Assurance
- Customs & Freight
- Retail
- Catering & Equipment Hire
2. Website – www.vnq-sample.com.pg
3. Phone – 345 6710 / 345 6722
4. Address – Sec 212, Lot 8. Kewana Rd, Tatuna
5. And logos of all our retail brands.
I have attached each of our logos. I have also attached a tribal fish design which we use on all business cards, email signatures and uniforms across all sites.
- Vela Nu Logo
- Grill Yard Logo
- Condor Wraps Logo
- Reefies Logo
- Tam Lok Ret Logo
- Bova Lulu Catering Logo
- Oven Loft Logo (for Vela Nu - Bakery Factory Products)
- Bova Fine logo (for Vela Nu - Butchery Factory Products)
- QSVER logo (Quality Assurance cert of our Butchery Factory)
Information that will change:
Name – e.g. Peter Olo
Title – Marketing & Promotions
Email –peterolo@velanusample.com.pg
Mobile – (+675 7222 2222)
Please use Peter Olo as an example in your designs.
Thank you and looking forward to your designs :)
Miriam
Target Market(s)
Local and International Clients
Industry/Entity Type
Food Industry
Contact Information for Business Card
See detailed brief

```html
<!DOCTYPE html>
<html lang="en">
<head>
<meta charset="utf-8">
<title>Vela Nu PNG LTD – Business Card</title>
<link rel="stylesheet" href="https://fonts.googleapis.com/css2?family=Sora:wght@300;400;500;600&display=swap">
<style>
:root{
  --scene:#f6d3d3;
  --white:#ffffff;
  --ink:#161616;
  --red:#e3342f;
  --red-band:#e9504d;
  --red-deep:#e8412c;
  --blush:#fdecee;
  --grey:#9a9a9a;
}
*{box-sizing:border-box;margin:0;padding:0}
html,body{width:818px;height:1200px;overflow:hidden}
body{background:var(--scene);font-family:"Sora",sans-serif;color:var(--ink);position:relative}
.card{position:absolute;top:274px;width:372px;height:651px;background:var(--white);overflow:hidden}
.card--front{left:19px}
.card--back{left:427px}

/* front */
.brand-mark{position:absolute;left:0;top:112px;width:372px;text-align:center}
.brand-mark__name{font-size:38px;font-weight:600;color:var(--ink);letter-spacing:.5px}
.brand-mark__sub{display:block;font-size:11px;font-weight:600;color:var(--ink);letter-spacing:1px;margin-top:2px}
.tribal-fish{position:absolute;left:238px;top:290px;width:118px;height:172px;border-radius:50% 40% 45% 50%;background:linear-gradient(160deg,rgba(200,200,200,.35),rgba(230,230,230,.12));}
.staff{position:absolute;left:48px;top:252px}
.staff__name{font-size:34px;font-weight:500;line-height:1.1}
.staff__rule{width:200px;height:2px;background:var(--red);margin:6px 0 7px}
.staff__title{font-size:15.5px;font-weight:400}
.contacts{position:absolute;left:48px;top:356px;list-style:none}
.contacts li{display:flex;align-items:center;height:26px;font-size:14.5px;font-weight:400;letter-spacing:-.2px}
.contacts svg{width:12px;height:12px;margin-right:11px;fill:var(--red)}
.front-band{position:absolute;left:0;top:477px;width:372px;height:8px;background:var(--red-band)}
.brand-grid{position:absolute;left:0;top:485px;width:372px;height:166px;display:grid;grid-template-columns:repeat(4,1fr);grid-template-rows:repeat(2,1fr)}
.brand-grid__cell{display:flex;align-items:center;justify-content:center;text-align:center;font-size:11px;font-weight:600;color:var(--red);line-height:1.15;padding:4px}
.brand-grid__cell--tint{background:var(--blush)}
.brand-grid__cell--dark{color:var(--ink)}
.cert-badge{width:48px;height:26px;border-radius:4px;background:var(--ink)}

/* back */
.product-grid{position:absolute;left:0;top:0;width:372px;height:469px;display:grid;grid-template-columns:1fr 1fr;grid-template-rows:repeat(3,1fr)}
.product-grid__cell{display:flex;align-items:center;justify-content:center;background:var(--white)}
.product-grid__cell--tint{background:var(--blush)}
.product-photo{width:140px;height:96px;border-radius:48%}
.product-photo--burger{background:radial-gradient(ellipse at 40% 50%,#b5652a 0%,#e0a84a 45%,rgba(240,200,120,.3) 75%,transparent 80%)}
.product-photo--beef{background:radial-gradient(ellipse,#a8313f 0%,#7a1e2a 45%,#2a2a2a 62%,transparent 68%)}
.product-photo--bread{background:radial-gradient(ellipse,#a5662c 0%,#8a4d22 45%,rgba(180,120,70,.3) 70%,transparent 76%)}
.product-photo--chicken{background:radial-gradient(ellipse,#f1cdb6 0%,#e7b49a 45%,rgba(230,180,160,.3) 70%,transparent 76%)}
.product-photo--sausage{background:radial-gradient(ellipse,#f2b38e 0%,#eea27a 45%,rgba(240,170,130,.3) 70%,transparent 76%)}
.product-photo--salmon{background:radial-gradient(ellipse,#f59a74 0%,#f2845c 40%,rgba(220,220,215,.8) 60%,transparent 72%)}
.name-band{position:absolute;left:0;top:469px;width:372px;height:71px;background:var(--red-band);color:var(--white)}
.name-band__title{position:absolute;left:25px;top:13px;font-size:27px;font-weight:400;letter-spacing:-.5px}
.name-band__sub{position:absolute;left:108px;top:44px;font-size:12px;font-weight:300}
.name-band__tag{position:absolute;left:170px;top:19px;height:19px;padding:0 6px;background:var(--white);color:var(--red);font-size:10.5px;font-weight:400;display:flex;align-items:center;letter-spacing:-.2px}
.services{position:absolute;left:0;top:540px;width:372px;height:111px;background:var(--red-deep);display:grid;grid-template-columns:105px 115px 132px;grid-template-rows:1fr 1fr;padding:12px 0 10px 20px;color:var(--white)}
.service{display:flex;align-items:center;font-size:10.5px;font-weight:300;line-height:1.25}
.service svg{width:24px;height:24px;margin-right:6px;flex:none;fill:none;stroke:var(--white);stroke-width:1.3;stroke-linejoin:round;stroke-linecap:round}
</style>
</head>
<body>

<section class="card card--front" aria-label="Business card front">
  <div class="brand-mark">
    <span class="brand-mark__name">Vela Nu</span>
    <span class="brand-mark__sub">PNG LTD</span>
  </div>

  <div class="tribal-fish" role="img" aria-label="Faint tribal fish design"></div>

  <div class="staff">
    <h1 class="staff__name">Peter Olo</h1>
    <div class="staff__rule"></div>
    <p class="staff__title">Marketing &amp; Promotions</p>
  </div>

  <ul class="contacts">
    <li><svg viewBox="0 0 12 12"><circle cx="6" cy="6" r="5.5"/><path d="M1 6h10M6 .5c2 2 2 9 0 11M6 .5c-2 2-2 9 0 11" stroke="#fff" stroke-width=".9" fill="none"/></svg>www.vnq-sample.com.pg</li>
    <li><svg viewBox="0 0 12 12"><path d="M2.4.6l2 2.4-1.2 1.6c.8 1.7 2.1 3 3.8 3.8l1.6-1.2 2.4 2-1.2 2.2C5 11.2.8 7 .2 1.8z"/></svg>345 6710 / 345 6722</li>
    <li><svg viewBox="0 0 12 12"><path d="M.5 2h11v8H.5z"/><path d="M.5 2.4L6 6.5l5.5-4.1" stroke="#fff" stroke-width="1" fill="none"/></svg>peterolo@velanusample.com.pg</li>
    <li><svg viewBox="0 0 12 12"><path d="M6 .3a4.2 4.2 0 0 0-4.2 4.2C1.8 7.6 6 11.7 6 11.7s4.2-4.1 4.2-7.2A4.2 4.2 0 0 0 6 .3zm0 6a1.7 1.7 0 1 1 0-3.4 1.7 1.7 0 0 1 0 3.4z"/></svg>Sec 212, Lot 8. Kewana Rd, Tatuna</li>
  </ul>

  <div class="front-band"></div>

  <div class="brand-grid">
    <div class="brand-grid__cell brand-grid__cell--tint">Bova Lulu</div>
    <div class="brand-grid__cell">Grill Yard</div>
    <div class="brand-grid__cell brand-grid__cell--tint">Condor Wraps</div>
    <div class="brand-grid__cell brand-grid__cell--dark">Reefies</div>
    <div class="brand-grid__cell brand-grid__cell--dark">Bova Oven Loft</div>
    <div class="brand-grid__cell brand-grid__cell--tint">Bova Fine</div>
    <div class="brand-grid__cell">Tam Lok Ret</div>
    <div class="brand-grid__cell brand-grid__cell--tint"><span class="cert-badge" role="img" aria-label="Certification badge"></span></div>
  </div>
</section>

<section class="card card--back" aria-label="Business card back">
  <div class="product-grid">
    <div class="product-grid__cell"><div class="product-photo product-photo--burger" role="img" aria-label="Cheeseburger with fries"></div></div>
    <div class="product-grid__cell product-grid__cell--tint"><div class="product-photo product-photo--beef" role="img" aria-label="Raw beef on a plate with lettuce"></div></div>
    <div class="product-grid__cell product-grid__cell--tint"><div class="product-photo product-photo--bread" role="img" aria-label="Bread rolls and loaf"></div></div>
    <div class="product-grid__cell"><div class="product-photo product-photo--chicken" role="img" aria-label="Fresh uncooked chicken"></div></div>
    <div class="product-grid__cell"><div class="product-photo product-photo--sausage" role="img" aria-label="Sausages"></div></div>
    <div class="product-grid__cell product-grid__cell--tint"><div class="product-photo product-photo--salmon" role="img" aria-label="Fresh salmon steak with lime"></div></div>
  </div>

  <div class="name-band">
    <h2 class="name-band__title">VELA NU</h2>
    <span class="name-band__tag">Wholesale Food Sales &amp; Delivery</span>
    <span class="name-band__sub">PNG LTD</span>
  </div>

  <div class="services">
    <div class="service"><svg viewBox="0 0 24 24"><path d="M3 4h18v4H3zM4 8v12h16V8M6 12h5v8M14 12h4v4h-4z"/></svg>Retailer<br>Store</div>
    <div class="service"><svg viewBox="0 0 24 24"><path d="M12 2l2.5 2 3-.3.7 3 2.6 1.6-1.2 2.8 1.2 2.8-2.6 1.6-.7 3-3-.3L12 22l-2.5-2-3 .3-.7-3-2.6-1.6 1.2-2.8-1.2-2.8 2.6-1.6.7-3 3 .3z"/><path d="M8.5 12l2.5 2.5 4.5-5"/></svg>Quality<br>Assurance</div>
    <div class="service"><svg viewBox="0 0 24 24"><path d="M3 15c0-5 5-8 10-8s8 2 8 5-3 6-9 6-9-1-9-3z"/><path d="M8 10l2 6M12 9l1.5 7M16 9l1 6"/></svg>Bakery<br>Manufacturing</div>
    <div class="service"><svg viewBox="0 0 24 24"><path d="M3 7h14v13H3zM3 11h14M7 15h6"/><circle cx="19" cy="6" r="3"/></svg>Customs<br>and Freight</div>
    <div class="service"><svg viewBox="0 0 24 24"><path d="M6 4c4-2 10-1 12 3s1 10-4 13-10 0-10-5 0-9 2-11z"/><path d="M8 9l8 6M16 9l-8 6"/></svg>Butchery<br>Manufacturing</div>
    <div class="service"><svg viewBox="0 0 24 24"><path d="M3 17h18M5 17a7 7 0 0 1 14 0M12 8V6M10 6h4M3 20h12"/></svg>Catering and<br>Equipment Hire</div>
  </div>
</section>

</body>
</html>
```